IT services company requires Letterhead design

We need a professional letterhead designed to be used for general correspondence with customers, quotes, invoices etc. We are a new IT services company specialising in computer servicing and repairs and mobile and tablet repairs. Attached are templates that my printing company have supplied, my logos, an interpretation of our website for you to get a feel of the company. Details to be included on the letterhead are

Company Number – 4830517
VAT Number - 581736294
Registered Address – 14-16 Brambury Lane, London, E9 3PL

Phone – 01843 572236
Email – sales@quorvant.com
Web – www.quorvant.com

I would prefer for the top of the letterhead to just have the company logo on a white background and the rest of the details on the bottom of the letterhead but I am open to design ideas.

Thanks

```html
<!DOCTYPE html>
<html lang="en">
<head>
<meta charset="utf-8">
<title>Quorvant Letterhead</title>
<link rel="stylesheet" href="https://fonts.googleapis.com/css2?family=Arimo:wght@400;700&display=swap">
<style>
  :root {
    --brand-cyan: #2ec2e3;
    --ink-dark: #3b3c3e;
    --ink-footer: #1c1f22;
    --paper: #ffffff;
  }
  html, body {
    margin: 0;
    padding: 0;
    width: 934px;
    height: 1200px;
    overflow: hidden;
    background: var(--paper);
  }
  .letterhead {
    position: relative;
    width: 934px;
    height: 1200px;
    background: var(--paper);
    font-family: "Arimo", Arial, sans-serif;
    overflow: hidden;
  }
  .top-marker {
    position: absolute;
    left: 24px;
    top: 0;
  }
  .brand {
    position: absolute;
    left: 22px;
    top: 58px;
    display: flex;
    align-items: center;
    gap: 12px;
  }
  .brand-square {
    width: 20px;
    height: 20px;
    background: var(--brand-cyan);
  }
  .brand-name {
    font-size: 80px;
    font-weight: 700;
    color: var(--ink-dark);
    letter-spacing: -2px;
    line-height: 1;
  }
  .footer-band {
    position: absolute;
    left: 0;
    top: 1090px;
  }
  .footer-text {
    position: absolute;
    color: var(--ink-footer);
    font-size: 16.5px;
    line-height: 1;
    white-space: nowrap;
  }
  .registration { left: 76px; top: 1142px; }
  .registration p { margin: 0 0 12px 0; }
  .address {
    right: 24px;
    top: 1118px;
    text-align: right;
    display: flex;
    gap: 6px;
  }
  .address-lines p { margin: 0 0 7px 0; }
  .contact-row {
    right: 24px;
    top: 1170px;
    display: flex;
    align-items: center;
  }
  .contact-item {
    display: flex;
    align-items: center;
    gap: 6px;
  }
  .contact-divider {
    width: 1px;
    height: 18px;
    background: rgba(255,255,255,0.45);
    margin: 0 12px;
  }
</style>
</head>
<body>
<main class="letterhead">
  <svg class="top-marker" width="54" height="29" viewBox="0 0 54 29" aria-hidden="true">
    <polygon points="0,0 54,0 27,29" fill="var(--brand-cyan)"/>
  </svg>

  <header class="brand">
    <span class="brand-name">Quorvant</span>
    <span class="brand-square"></span>
  </header>

  <svg class="footer-band" width="934" height="110" viewBox="0 0 934 110" aria-hidden="true">
    <polygon points="0,0 44,0 86,31 128,0 934,0 934,110 0,110" fill="var(--brand-cyan)"/>
  </svg>

  <div class="footer-text registration">
    <p>VAT No. - 581736294</p>
    <p>Company No. – 4830517</p>
  </div>

  <div class="footer-text address">
    <svg width="13" height="18" viewBox="0 0 13 18" aria-hidden="true">
      <path d="M6.5 0C2.9 0 0 2.8 0 6.3 0 11 6.5 18 6.5 18S13 11 13 6.3C13 2.8 10.1 0 6.5 0z" fill="#fff"/>
      <circle cx="6.5" cy="6.3" r="2.4" fill="var(--brand-cyan)"/>
    </svg>
    <div class="address-lines">
      <p>14-16 Brambury Lane</p>
      <p>London E9 3PL</p>
    </div>
  </div>

  <div class="footer-text contact-row">
    <span class="contact-item">
      <svg width="16" height="16" viewBox="0 0 16 16" aria-hidden="true">
        <circle cx="8" cy="8" r="7" fill="none" stroke="#fff" stroke-width="1.4"/>
        <path d="M6 4.5l1.3 1.6-.8 1c.5 1 1.2 1.8 2.1 2.3l1-.8 1.6 1.3-.9 1.3C7.7 11 5.1 8.3 4.6 5.3z" fill="#fff"/>
      </svg>
      01843 572236
    </span>
    <span class="contact-divider"></span>
    <span class="contact-item">
      <svg width="18" height="13" viewBox="0 0 18 13" aria-hidden="true">
        <rect x="0" y="0" width="18" height="13" fill="#fff"/>
        <polyline points="0,0 9,7 18,0" fill="none" stroke="var(--brand-cyan)" stroke-width="1.4"/>
      </svg>
      sales@quorvant.com
    </span>
    <span class="contact-divider"></span>
    <span class="contact-item">
      <svg width="15" height="15" viewBox="0 0 15 15" aria-hidden="true">
        <g fill="none" stroke="#fff" stroke-width="1.1">
          <circle cx="7.5" cy="7.5" r="6.8"/>
          <ellipse cx="7.5" cy="7.5" rx="3" ry="6.8"/>
          <line x1="0.7" y1="7.5" x2="14.3" y2="7.5"/>
          <line x1="7.5" y1="0.7" x2="7.5" y2="14.3"/>
        </g>
      </svg>
      www.quorvant.com
    </span>
  </div>
</main>
</body>
</html>
```